Redesign wellness clinic website

The project is redesign a wellness clinic http://www.thornleighvitality.example. The new website is to be responsive,clean,bright and a strong call to action which is to book an appointment. The logo will remain the same but the colour scheme on the website should be reflect purple white and green. I want it to be bright and cheerful and the feeling of clarity. The website shouldn't be overloaded with content but more visuals.

Target Market(s)

Anyone that has corporate wellness benefits within the downtown Toronto core. Majority of audience are professional working in Media, Telecommunications and Investments.

Industry/Entity Type

Health And Wellness

Number of Pages Required

5+ page

Font styles to use
Sans Serif

Colors
ffffff
886aae
acd036

Requirements
Must have
• -Strong call to action which is book an appointment like this page https://www.kestrelmotion.example/
• -Services provided icons on the page like https://www.brightpathvitalityhouse.example/
• - Pictures of a good visualizing a fit and healthy life
• - Strong ratings from Quorva, Zintrel, PostMaz, similar to this website http://www.summitbalancehealth.example/our-team-professionals/
• - Bright and clear
Should not have
• -No black and white images (redo our pictures)
• -Dark themes

```html
<!DOCTYPE html>
<html lang="en">
<head>
<meta charset="utf-8">
<title>Thornleigh Vitality Centre</title>
<link rel="stylesheet" href="https://fonts.googleapis.com/css2?family=Anton&family=Montserrat:wght@400;500;600;700&display=swap">
<style>
:root{
  --purple:#886aae;
  --purple-dark:#6f5593;
  --green:#acd036;
  --green-soft:#f1f7dd;
  --orange:#f0a24a;
  --white:#ffffff;
  --grey-bg:#f3f3f3;
  --grey-line:#e2e2e2;
  --text:#555555;
  --text-light:#8c8c8c;
  --dark:#333333;
}
*{box-sizing:border-box;margin:0;padding:0}
html,body{width:1200px;height:4467px;overflow:hidden}
body{font-family:"Montserrat",sans-serif;color:var(--text);background:var(--white);font-size:13px;line-height:1.6}
.display{font-family:"Anton",sans-serif;font-weight:400;letter-spacing:1px;text-transform:uppercase}
.btn{display:inline-block;font-size:11px;font-weight:700;letter-spacing:1px;text-transform:uppercase;color:var(--white);padding:10px 26px}
.btn--green{background:var(--green)}
.btn--purple{background:var(--purple)}
.eyebrow{color:var(--green);font-weight:700;font-size:13px;letter-spacing:1px;text-transform:uppercase}

/* top bar */
.topbar{height:36px;background:var(--purple);display:flex;align-items:center;justify-content:space-between;color:var(--white);font-size:11px;font-weight:600;letter-spacing:1px;padding-left:24px}
.topbar__actions{display:flex;height:100%}
.topbar__search{width:36px;background:var(--green);display:flex;align-items:center;justify-content:center}
.topbar__book{background:var(--dark);display:flex;align-items:center;gap:8px;padding:0 22px;text-transform:uppercase}

/* nav */
.nav{height:62px;display:flex;align-items:center;justify-content:space-between;padding:0 24px;font-size:11px;font-weight:600;letter-spacing:1px;text-transform:uppercase;color:var(--dark);border-bottom:1px solid var(--grey-line)}
.nav ul{display:flex;list-style:none;gap:58px}
.brand{display:flex;align-items:center;gap:8px;font-size:12px;font-weight:700;color:var(--purple);text-transform:none;letter-spacing:0}
.brand__mark{width:28px;height:28px;border-radius:50%;background:var(--purple)}

/* hero */
.hero{position:relative;height:564px;display:flex;flex-direction:column;align-items:center;justify-content:center;text-align:center;color:var(--white)}
.hero__photo{position:absolute;inset:0;background:linear-gradient(120deg,#b6d64c 0%,#c9e27a 40%,#a6c93b 70%,#93b82f 100%)}
.hero__content{position:relative}
.hero h1{font-size:50px;line-height:1.15;margin-bottom:14px;text-shadow:0 2px 6px rgba(0,0,0,.25)}
.hero h2{font-size:22px;margin-bottom:32px;text-shadow:0 2px 6px rgba(0,0,0,.25)}
.dots{display:flex;gap:8px;justify-content:center;margin-top:48px}
.dots span{width:10px;height:10px;border-radius:50%;background:rgba(255,255,255,.6)}
.dots span.on{background:var(--white)}

/* about */
.about{height:523px;display:flex;justify-content:space-between;padding:80px 110px 0 160px;background:linear-gradient(180deg,#f7f7f7 0%,#fff 30%)}
.about__text{width:460px}
.about h2{font-size:38px;color:var(--purple);line-height:1}
.about p{font-size:12px;margin-top:14px}
.about__tags{display:flex;gap:14px;margin:26px 0}
.tag{display:flex;align-items:center;gap:8px;border:1px solid var(--grey-line);padding:8px 14px;font-size:10px;font-weight:600;text-transform:uppercase;color:var(--dark)}
.about__photo{width:320px;height:440px;background:linear-gradient(180deg,#eef0f3 0%,#d8dde4 55%,#2f3a4e 56%,#243044 100%)}

/* values */
.values{height:221px;background:var(--grey-bg);display:flex;justify-content:center;gap:50px;padding-top:50px}
.value{width:270px;display:flex;gap:16px}
.value svg{flex:0 0 54px}
.value h3{font-family:"Anton",sans-serif;font-weight:400;color:var(--purple);font-size:22px;line-height:1.1;letter-spacing:1px;text-transform:uppercase}
.value p{font-size:11px;line-height:1.5}

/* services */
.services{height:828px;background:var(--purple);color:var(--white);text-align:center;padding-top:70px}
.services h2{font-size:38px;line-height:1}
.services__intro{width:560px;margin:22px auto 40px;font-size:11px}
.service-grid{display:flex;flex-wrap:wrap;justify-content:center;gap:30px 56px;width:960px;margin:0 auto}
.service{width:180px}
.service__icon{width:112px;height:112px;border-radius:50%;background:var(--white);margin:0 auto 12px;display:flex;align-items:center;justify-content:center}
.service h3{font-size:13px;font-weight:700;text-transform:uppercase;line-height:1.3}
.service p{font-size:11px;color:#e3daef;line-height:1.5;margin-top:6px}
.services .btn{margin-top:40px}

/* location */
.location{height:342px;display:flex}
.location__map{width:600px;position:relative;background:linear-gradient(135deg,#f2f2f2,#e7e7e7)}
.location__text{position:absolute;left:160px;top:60px;width:330px}
.location h2{color:var(--purple);font-size:36px;line-height:1}
.location h4{color:var(--green);font-size:13px;font-weight:700;margin:16px 0 10px;text-transform:uppercase}
.location p{font-size:12px;margin-bottom:16px}
.location__pitch{width:600px;padding:70px 0 0 32px;color:var(--text-light)}
.location__pitch .lead{font-size:22px;line-height:1.35;color:var(--text)}
.location__pitch .small{font-size:12px;letter-spacing:1px;text-align:center;margin:16px 80px 14px 0;text-transform:uppercase}
.location__pitch .cta{font-size:20px;font-weight:600;color:var(--purple)}
.location__pitch .cta span{color:var(--green)}

/* testimonials */
.testimonials{height:447px;background:var(--green-soft);text-align:center;padding-top:60px}
.section-title{font-size:38px;color:var(--purple);line-height:1}
.avatar{width:100px;height:100px;border-radius:50%;background:linear-gradient(160deg,#dcdcdc,#b9b9b9);margin:26px auto 16px}
.testimonials blockquote{width:700px;margin:0 auto;font-size:12px}
.testimonials cite{display:block;font-style:normal;font-weight:700;color:var(--dark);font-size:12px;margin-top:22px}
.testimonials small{display:block;font-size:10px;color:var(--text-light)}
.testimonials .dots{margin-top:14px}
.testimonials .dots span{background:#cfd8b0}
.testimonials .dots span.on{background:var(--green)}

/* blog */
.blog{height:595px;text-align:center;padding-top:50px}
.blog__grid{display:flex;justify-content:center;gap:28px;margin-top:40px}
.post{width:276px;background:var(--white);box-shadow:0 2px 8px rgba(0,0,0,.1);padding-bottom:20px}
.post__img{height:246px}
.post h3{font-size:14px;font-weight:700;color:var(--dark);margin:18px 18px 6px;text-align:left}
.post p{font-size:11px;text-align:left;margin:0 18px 20px;line-height:1.5}
.post a{font-size:10px;font-weight:700;letter-spacing:1px;color:var(--purple)}

/* ratings */
.ratings{height:230px;display:flex;justify-content:center;gap:28px;padding-top:10px}
.rating{width:200px;height:190px;box-shadow:0 2px 8px rgba(0,0,0,.1);display:flex;flex-direction:column;align-items:center;justify-content:center;text-align:center;gap:6px;font-size:11px}
.rating__name{display:flex;align-items:center;gap:6px;font-size:20px;font-weight:700;color:var(--dark)}
.rating__name i{width:14px;height:14px;border-radius:50%;background:var(--purple);display:inline-block}
.stars{color:#f5a623;font-size:18px;letter-spacing:2px}

/* newsletter */
.newsletter{height:143px;background:linear-gradient(180deg,#fff 0%,#f3f3f3 100%);padding-top:20px}
.newsletter__box{width:880px;height:102px;margin:0 auto;background:var(--white);box-shadow:0 2px 8px rgba(0,0,0,.08);display:flex;align-items:center;padding:0 50px;gap:60px}
.newsletter h3{font-size:26px;color:var(--purple);line-height:1}
.newsletter__form{display:flex;align-items:center;gap:10px;flex:1}
.newsletter__input{flex:1;border-bottom:1px solid var(--grey-line);font-size:11px;color:var(--text-light);padding:8px 0}

/* footer */
.footer{height:268px;background:var(--grey-bg);display:flex;gap:70px;padding:30px 0 0 160px;font-size:11px}
.footer h4{font-size:12px;font-weight:700;color:var(--dark);text-transform:uppercase;margin-bottom:10px}
.footer ul{list-style:none;line-height:1.7}
.footer__contact li{display:flex;gap:8px;align-items:flex-start}
.footer__contact svg{margin-top:3px;flex:0 0 auto}
.footer li.bullet::before{content:"›";color:var(--purple);margin-right:6px}
.partner{margin-left:20px;width:200px;height:120px;border:1px solid var(--grey-line);background:var(--white);display:flex;flex-direction:column;align-items:center;justify-content:center;gap:6px}
.partner span{font-size:9px;font-weight:700;text-transform:uppercase;color:var(--text-light)}
.partner strong{font-size:18px;color:var(--dark)}

/* bottom */
.bottom{height:209px;background:var(--white);text-align:center;padding-top:30px;font-size:10px;color:var(--text-light)}
.badge{width:60px;height:70px;margin:0 auto 14px;background:var(--orange);border-radius:4px}
.bottom p{margin-bottom:16px}
.social{display:flex;justify-content:center;gap:18px;margin-top:6px}
.social span{width:10px;height:10px;border-radius:50%;background:var(--dark)}
</style>
</head>
<body>

<header>
  <div class="topbar">
    <span>WELCOME TO THORNLEIGH VITALITY CENTRE</span>
    <div class="topbar__actions">
      <div class="topbar__search"><svg width="14" height="14" viewBox="0 0 14 14"><circle cx="6" cy="6" r="4.5" fill="none" stroke="#fff" stroke-width="1.6"/><line x1="9.3" y1="9.3" x2="13" y2="13" stroke="#fff" stroke-width="1.6"/></svg></div>
      <div class="topbar__book">Book an appointment <svg width="14" height="14" viewBox="0 0 14 14"><circle cx="7" cy="7" r="6.5" fill="#fff"/><path d="M5.5 4l3 3-3 3" fill="none" stroke="#333" stroke-width="1.5"/></svg></div>
    </div>
  </div>
  <nav class="nav">
    <ul><li>Fees and Services</li><li>Our Staff</li><li>News and Updates</li></ul>
    <div class="brand"><span class="brand__mark"></span>Thornleigh Vitality Centre</div>
    <ul><li>Corporate Wellness</li><li>Forms</li><li>Contact Us</li></ul>
  </nav>
</header>

<section class="hero">
  <div class="hero__photo" role="img" aria-label="Therapist giving a relaxing massage in soft green light"></div>
  <div class="hero__content">
    <h1 class="display">Relieve aches and<br>experience deep relaxation</h1>
    <h2 class="display">Massage from one of our registered therapists</h2>
    <span class="btn btn--purple">Book an appointment</span>
    <div class="dots"><span class="on"></span><span></span><span></span><span></span></div>
  </div>
</section>

<section class="about">
  <div class="about__text">
    <h2 class="display">About us</h2>
    <div class="eyebrow">Established in 1989</div>
    <p>Lorem Ipsum is simply dummy text of the printing and typesetting industry.</p>
    <p>Lorem Ipsum has been the industry's standard dummy text ever since the 1500s, when an unknown printer took a galley of type and scrambled it to make a type specimen book.</p>
    <p>It has survived not only five centuries, but also the leap into electronic typesetting, remaining essentially unchanged. It was popularised in the 1960s with the release of Letraset sheets containing Lorem Ipsum passages, and more recently with desktop publishing software including versions of Lorem Ipsum.</p>
    <div class="about__tags">
      <span class="tag"><svg width="14" height="14" viewBox="0 0 14 14"><circle cx="7" cy="7" r="6" fill="none" stroke="#acd036" stroke-width="1.5"/><path d="M4 7l2 2 4-4" fill="none" stroke="#acd036" stroke-width="1.5"/></svg>Ranked as a top wellness centre</span>
      <span class="tag"><svg width="14" height="14" viewBox="0 0 14 14"><circle cx="7" cy="7" r="6" fill="none" stroke="#acd036" stroke-width="1.5"/><path d="M4 7l2 2 4-4" fill="none" stroke="#acd036" stroke-width="1.5"/></svg>Professional team</span>
    </div>
    <span class="btn btn--green">Read more</span>
  </div>
  <div class="about__photo" role="img" aria-label="Smiling clinic director in a dark suit"></div>
</section>

<section class="values">
  <div class="value">
    <svg width="54" height="54" viewBox="0 0 54 54"><circle cx="27" cy="27" r="22" fill="none" stroke="#acd036" stroke-width="2"/><line x1="12" y1="27" x2="42" y2="27" stroke="#acd036" stroke-width="2"/><line x1="27" y1="15" x2="27" y2="39" stroke="#acd036" stroke-width="2"/></svg>
    <div><h3>Balance</h3><p>Lorem Ipsum has been the industry's standard dummy text ever since the 1500s, when an unknown printer took a galley of type and scrambled it to make a type specimen book.</p></div>
  </div>
  <div class="value">
    <svg width="54" height="54" viewBox="0 0 54 54"><circle cx="27" cy="27" r="22" fill="none" stroke="#acd036" stroke-width="2"/><path d="M27 38s-10-6-10-13a5 5 0 0110-2 5 5 0 0110 2c0 7-10 13-10 13z" fill="none" stroke="#acd036" stroke-width="2"/></svg>
    <div><h3>Healthy</h3><p>Lorem Ipsum has been the industry's standard dummy text ever since the 1500s, when an unknown printer took a galley of type and scrambled it to make a type specimen book.</p></div>
  </div>
  <div class="value">
    <svg width="54" height="54" viewBox="0 0 54 54"><circle cx="27" cy="27" r="22" fill="none" stroke="#acd036" stroke-width="2"/><path d="M18 32c2-10 12-14 18-14-1 10-7 16-18 14z" fill="none" stroke="#acd036" stroke-width="2"/></svg>
    <div><h3>Fresh</h3><p>Lorem Ipsum has been the industry's standard dummy text ever since the 1500s, when an unknown printer took a galley of type and scrambled it to make a type specimen book.</p></div>
  </div>
</section>

<section class="services">
  <h2 class="display">Services</h2>
  <div class="eyebrow">What we doing</div>
  <p class="services__intro">Lorem Ipsum has been the industry's standard dummy text ever since the 1500s, when an unknown printer took a galley of type and scrambled it to make a type specimen book.</p>
  <div class="service-grid">
    <div class="service"><div class="service__icon" role="img" aria-label="Chiropractic icon"><svg width="40" height="40"><rect x="16" y="4" width="8" height="32" rx="4" fill="none" stroke="#886aae" stroke-width="2"/></svg></div><h3>Chiropractic</h3><p>Lorem Ipsum is simply dummy text of the printing and typesetting industry.</p></div>
    <div class="service"><div class="service__icon" role="img" aria-label="Physiotherapy icon"><svg width="40" height="40"><circle cx="20" cy="8" r="4" fill="none" stroke="#886aae" stroke-width="2"/><line x1="20" y1="12" x2="20" y2="36" stroke="#886aae" stroke-width="2"/></svg></div><h3>Physiotherapy</h3><p>Lorem Ipsum is simply dummy text of the printing and typesetting industry.</p></div>
    <div class="service"><div class="service__icon" role="img" aria-label="Active rehabilitation icon"><svg width="40" height="40"><line x1="8" y1="34" x2="32" y2="6" stroke="#886aae" stroke-width="2"/><circle cx="30" cy="30" r="4" fill="none" stroke="#886aae" stroke-width="2"/></svg></div><h3>Active rehabilitation</h3><p>Lorem Ipsum is simply dummy text of the printing and typesetting industry.</p></div>
    <div class="service"><div class="service__icon" role="img" aria-label="Massage therapy icon"><svg width="40" height="40"><rect x="4" y="22" width="32" height="8" rx="4" fill="none" stroke="#886aae" stroke-width="2"/><circle cx="12" cy="14" r="4" fill="none" stroke="#886aae" stroke-width="2"/></svg></div><h3>Massage therapy</h3><p>Lorem Ipsum is simply dummy text of the printing and typesetting industry.</p></div>
    <div class="service"><div class="service__icon" role="img" aria-label="Nutrition icon"><svg width="40" height="40"><rect x="8" y="6" width="24" height="28" rx="2" fill="none" stroke="#886aae" stroke-width="2"/><line x1="13" y1="14" x2="27" y2="14" stroke="#886aae" stroke-width="2"/><line x1="13" y1="20" x2="27" y2="20" stroke="#886aae" stroke-width="2"/></svg></div><h3>Nutrition and lifestyle medicine</h3><p>Lorem Ipsum is simply dummy text of the printing and typesetting industry.</p></div>
    <div class="service"><div class="service__icon" role="img" aria-label="Chiropody icon"><svg width="40" height="40"><path d="M16 4v22c0 6 4 10 12 10" fill="none" stroke="#886aae" stroke-width="2"/></svg></div><h3>Chiropody</h3><p>Lorem Ipsum is simply dummy text of the printing and typesetting industry.</p></div>
    <div class="service"><div class="service__icon" role="img" aria-label="Osteopathy icon"><svg width="40" height="40"><path d="M14 36V14l6-8 6 8v22" fill="none" stroke="#886aae" stroke-width="2"/></svg></div><h3>Osteopathy</h3><p>Lorem Ipsum is simply dummy text of the printing and typesetting industry.</p></div>
  </div>
  <span class="btn btn--green">View all</span>
</section>

<section class="location">
  <div class="location__map" role="img" aria-label="Light street map around the new clinic location">
    <div class="location__text">
      <div class="eyebrow">Visit our</div>
      <h2 class="display">New location</h2>
      <h4>We are open for business at 7:30 am.<br>Open 7 days a week!</h4>
      <p>Ask one of our associates about<br>our Referral Reward Program</p>
      <span class="btn btn--green">View map</span>
    </div>
  </div>
  <div class="location__pitch">
    <p class="lead">Our Centre is committed to helping improve and extend the lives of as many people as possible in our community.</p>
    <p class="small">Come and join our family and start changing your life today.</p>
    <p class="cta">Planning a wellness fair? <span>We can help!</span></p>
    <p>Contact us at info@thornleighvitality.example</p>
  </div>
</section>

<section class="testimonials">
  <h2 class="section-title display">What our clients say</h2>
  <div class="eyebrow">Our happy clients</div>
  <div class="avatar" role="img" aria-label="Client portrait"></div>
  <blockquote>Lorem Ipsum has been the industry's standard dummy text ever since the 1500s, when an unknown printer took a galley of type and scrambled it to make a type specimen book.</blockquote>
  <cite>Nora Bellamy</cite>
  <small>Satisfied Customer</small>
  <div class="dots"><span></span><span class="on"></span><span></span></div>
</section>

<section class="blog">
  <h2 class="section-title display">Our blog</h2>
  <div class="blog__grid">
    <article class="post"><div class="post__img" role="img" aria-label="Spa stones, towels and candles" style="background:linear-gradient(160deg,#c9a77a,#f1ede6)"></div><h3>LOREM IPSUM IS SIMPLY TEXT</h3><p>Lorem Ipsum is simply dummy text of the printing and typesetting industry.</p><a>VIEW MORE</a></article>
    <article class="post"><div class="post__img" role="img" aria-label="Therapist massaging a client's back" style="background:linear-gradient(160deg,#e6c4a8,#b9876a)"></div><h3>LOREM IPSUM IS SIMPLY TEXT</h3><p>Lorem Ipsum is simply dummy text of the printing and typesetting industry.</p><a>VIEW MORE</a></article>
    <article class="post"><div class="post__img" role="img" aria-label="Hands during a therapy session" style="background:linear-gradient(160deg,#ece4f2,#d9b9a5)"></div><h3>LOREM IPSUM IS SIMPLY TEXT</h3><p>Lorem Ipsum is simply dummy text of the printing and typesetting industry.</p><a>VIEW MORE</a></article>
  </div>
</section>

<section class="ratings">
  <div class="rating"><div class="rating__name"><i></i>Vetrano</div><span>Dr. Alan Preston</span><span class="stars">★★★★☆</span><span>50 reviews</span></div>
  <div class="rating"><div class="rating__name"><i></i>Zintrel</div><span class="stars">★★★★★</span><span>Great Reviews on Zintrel</span></div>
  <div class="rating"><div class="rating__name"><i></i>Quorva</div><span class="stars">★★★★★</span><span>5 Star Rating on Quorva</span></div>
  <div class="rating"><div class="rating__name"><i></i>Healvista</div><span class="stars">★★★★★</span><span>Great Reviews on Healvista</span></div>
</section>

<section class="newsletter">
  <div class="newsletter__box">
    <div><div class="eyebrow">Let's get updated</div><h3 class="display">Subscribe newsletter</h3></div>
    <div class="newsletter__form"><span class="newsletter__input">Enter your email address</span><span class="btn btn--green">Subscribe</span></div>
  </div>
</section>

<footer class="footer">
  <div class="footer__contact">
    <h4>Contact us</h4>
    <ul>
      <li><svg width="10" height="14" viewBox="0 0 10 14"><path d="M5 0a5 5 0 015 5c0 4-5 9-5 9S0 9 0 5a5 5 0 015-5z" fill="#886aae"/></svg><span>48 Hollis Avenue, Suite 210<br>Toronto, Ontario<br>M9Q 2Z4</span></li>
      <li><svg width="12" height="12" viewBox="0 0 12 12"><path d="M2 1l2.5 0 1 3-1.5 1a7 7 0 003 3l1-1.5 3 1V11C5 11 1 7 1 2z" fill="#886aae"/></svg>416-555-0142</li>
      <li><svg width="12" height="10" viewBox="0 0 12 10"><rect width="12" height="10" fill="#886aae"/><path d="M0 0l6 5 6-5" fill="none" stroke="#fff"/></svg>info@thornleighvitality.example</li>
    </ul>
  </div>
  <div>
    <h4>Services</h4>
    <ul><li class="bullet">Chiropractic</li><li class="bullet">Physiotherapy</li><li class="bullet">Active Rehabilitation</li><li class="bullet">Massage Therapy</li><li class="bullet">Nutrition and Lifestyle Medicine</li><li class="bullet">Chiropody</li><li class="bullet">Osteopathy</li></ul>
  </div>
  <div>
    <h4>Quick links</h4>
    <ul><li class="bullet">Fees and Services</li><li class="bullet">Our Staff</li><li class="bullet">News and Updates</li><li class="bullet">Corporate Wellness</li><li class="bullet">Forms</li><li class="bullet">Contact</li></ul>
  </div>
  <div class="partner"><span>Our partner</span><strong>Marlow Dental</strong></div>
</footer>

<div class="bottom">
  <div class="badge" role="img" aria-label="Award badge"></div>
  <p>Thornleigh Vitality Centre is ranked as a top Wellness Centre in Toronto ON - verified by local listing.</p>
  <p>© 2017 Thornleigh Vitality Centre. All Rights Reserved.</p>
  <div class="social"><span></span><span></span><span></span><span></span></div>
</div>

</body>
</html>
```